Ad Design for a child care centre

Bright Pebbles Child Care Centre offers a safe, nurturing environment where your child will get the attention and care that he or she needs. Our ratio of children to adults is always within state guidelines - and often even higher - to make certain each child receives top-quality care
We are also state licensed as a Child Care facility and have met or exceeded all health and safety guidelines.
3-5 year Kinder Funded Program
Story Time
Show and Tell
Puzzles and Games
Computer Time
Arts and Crafts
Music
Pre-Reading Activities
And much more
You can rest assured that your child will be cared for with the most kindness, love and respect. We believe all children are precious gifts and we treat them as though they are our own.
Full-time, part-time, Half days, Before, after-school schedules are available.
To learn more, contact us today! 03 9514 -0817 or info@brightpebbles.example.au

```html
<!DOCTYPE html>
<html lang="en">
<head>
<meta charset="utf-8">
<title>Bright Pebbles Child Care Centre</title>
<link href="https://fonts.googleapis.com/css2?family=Arimo:wght@400;700&family=Roboto+Slab:wght@800&family=Roboto+Condensed:wght@700&display=swap" rel="stylesheet">
<style>
  :root {
    --sky-top: #c9d6ef;
    --sky-mid: #dfe7f6;
    --sky-low: #f3f6fc;
    --ink: #2b2b2b;
    --navy: #263a8c;
    --contact-blue: #1f4196;
    --frame-blue: #2f7fd0;
    --panel: #b7c6e6;
    --band-red: #d5202a;
    --brand: #e8561f;
    --white: #ffffff;
  }
  * { margin: 0; padding: 0; box-sizing: border-box; }
  html, body { width: 849px; height: 1200px; overflow: hidden; }
  body {
    position: relative;
    font-family: "Arimo", Arial, sans-serif;
    color: var(--ink);
    background: linear-gradient(180deg, var(--sky-top) 0%, var(--sky-mid) 35%, var(--sky-mid) 55%, var(--sky-low) 85%, var(--white) 100%);
  }
  .abs { position: absolute; }

  .brand-name {
    left: 0; right: 0; top: 52px;
    text-align: center;
    font-family: "Roboto Slab", Georgia, serif;
    font-weight: 800;
    font-size: 84px;
    line-height: 1;
    color: var(--brand);
  }
  .brand-sub {
    left: 0; right: 0; top: 186px;
    text-align: center;
    font-family: "Roboto Slab", Georgia, serif;
    font-weight: 800;
    font-size: 46px;
    line-height: 1.1;
    color: var(--ink);
  }
  .intro {
    left: 40px; right: 40px; top: 256px;
    text-align: center;
    font-size: 14.6px;
    line-height: 18.5px;
  }

  .gallery {
    left: 37px; top: 328px; width: 779px; height: 370px;
    background: var(--panel);
    border-radius: 6px;
    box-shadow: 0 2px 6px rgba(60, 80, 130, .35);
  }
  .photo {
    position: absolute;
    border: 2px solid var(--frame-blue);
    border-radius: 12px;
  }
  .photo--lead { left: 6px; top: 24px; width: 258px; height: 327px; background: linear-gradient(150deg, #d9b7a6, #c995a0 55%, #e3a8c0); }
  .photo--a1 { left: 276px; top: 24px; width: 88px; height: 157px; background: linear-gradient(160deg, #8aa86a, #c9a38c); }
  .photo--a2 { left: 377px; top: 24px; width: 88px; height: 157px; background: linear-gradient(160deg, #e8e6ee, #8c79b6); }
  .photo--a3 { left: 478px; top: 24px; width: 88px; height: 157px; background: linear-gradient(160deg, #a1456b, #7f9a56); }
  .photo--a4 { left: 579px; top: 24px; width: 88px; height: 157px; background: linear-gradient(160deg, #8a5a3c, #5a3b2e); }
  .photo--a5 { left: 680px; top: 24px; width: 88px; height: 157px; background: linear-gradient(160deg, #6b6157, #3d3a3c); }
  .photo--b1 { left: 276px; top: 193px; width: 88px; height: 158px; background: linear-gradient(160deg, #4f8a52, #b9454a); }
  .photo--b2 { left: 377px; top: 193px; width: 88px; height: 158px; background: linear-gradient(160deg, #6f86a8, #d2a27d); }
  .photo--b3 { left: 478px; top: 193px; width: 88px; height: 158px; background: linear-gradient(160deg, #d3b196, #b65a4e); }
  .photo--b4 { left: 579px; top: 193px; width: 88px; height: 158px; background: linear-gradient(160deg, #4a6da8, #a09a8a); }
  .photo--b5 { left: 680px; top: 193px; width: 88px; height: 158px; background: linear-gradient(160deg, #c7a0a8, #d7b49a); }

  .licence {
    left: 120px; right: 120px; top: 722px;
    text-align: center;
    font-size: 18.6px;
    line-height: 25px;
  }
  .program-title {
    left: 0; right: 0; top: 784px;
    text-align: center;
    font-family: "Roboto Slab", Georgia, serif;
    font-weight: 800;
    font-size: 33px;
    color: var(--navy);
  }
  .activities {
    list-style: none;
    font-weight: 700;
    font-variant: small-caps;
    font-size: 19px;
    letter-spacing: .6px;
    line-height: 31.5px;
    color: var(--ink);
    top: 832px;
  }
  .activities--left { left: 163px; }
  .activities--right { left: 443px; }
  .activities-divider {
    left: 405px; top: 842px; width: 1.5px; height: 108px;
    background: var(--ink);
  }
  .promise {
    left: 40px; right: 40px; top: 953px;
    text-align: center;
    font-size: 18.6px;
    line-height: 25px;
  }
  .schedule-band {
    left: 0; top: 1063px; width: 849px; height: 47px;
    background: var(--band-red);
    color: var(--white);
    font-family: "Roboto Condensed", "Arial Narrow", sans-serif;
    font-weight: 700;
    font-size: 21.5px;
    line-height: 47px;
    text-align: center;
  }
  .contact-lead {
    left: 127px; top: 1124px;
    font-size: 16.5px;
    color: var(--navy);
  }
  .contact-phone {
    left: 127px; top: 1145px;
    font-size: 37px;
    font-weight: 700;
    color: var(--contact-blue);
  }
  .contact-or {
    left: 408px; top: 1148px;
    font-size: 17px;
    color: var(--navy);
  }
  .contact-email {
    left: 449px; top: 1143px;
    font-size: 22px;
    font-weight: 700;
    color: var(--contact-blue);
  }
</style>
</head>
<body>
  <header>
    <div class="abs brand-name">Bright Pebbles</div>
    <h1 class="abs brand-sub">Child Care Centre</h1>
  </header>

  <p class="abs intro">offers a safe, nurturing environment where your child will get the attention and care that he or she needs.<br>Our ratio of children to adults is always within state guidelines - and often even higher - to make certain<br>each child receives top-quality care</p>

  <section class="abs gallery">
    <div class="photo photo--lead" role="img" aria-label="Photo of a baby lying on a pink polka-dot cushion"></div>
    <div class="photo photo--a1" role="img" aria-label="Photo of two young children at play"></div>
    <div class="photo photo--a2" role="img" aria-label="Photo of a toddler in a purple top"></div>
    <div class="photo photo--a3" role="img" aria-label="Photo of children playing outdoors on grass"></div>
    <div class="photo photo--a4" role="img" aria-label="Photo of a baby sitting on a wooden floor"></div>
    <div class="photo photo--a5" role="img" aria-label="Photo of a toddler pointing upward"></div>
    <div class="photo photo--b1" role="img" aria-label="Photo of children sitting on a play mat"></div>
    <div class="photo photo--b2" role="img" aria-label="Photo of a child with face paint"></div>
    <div class="photo photo--b3" role="img" aria-label="Photo of a smiling toddler"></div>
    <div class="photo photo--b4" role="img" aria-label="Photo of children in a classroom"></div>
    <div class="photo photo--b5" role="img" aria-label="Photo of two children in sun hats"></div>
  </section>

  <p class="abs licence">We are also state licensed as a Child Care facility and have met or exceeded all health and safety guidelines.</p>

  <h2 class="abs program-title">3-5 year Kinder Funded Program</h2>
  <ul class="abs activities activities--left">
    <li>Story Time</li>
    <li>Show and Tell</li>
    <li>Puzzles and Games</li>
    <li>Computer Time</li>
  </ul>
  <div class="abs activities-divider"></div>
  <ul class="abs activities activities--right">
    <li>Arts and Crafts</li>
    <li>Music</li>
    <li>Pre-Reading Activities</li>
    <li>And much more</li>
  </ul>

  <p class="abs promise">You can rest assured that your child will be cared for with the most kindness, love and respect. We believe all children are precious gifts and we treat them as though they are our own.</p>

  <div class="abs schedule-band">Full-time, Part-time, Half days, Before, After-School schedules are available.</div>

  <footer>
    <div class="abs contact-lead">To learn more, contact us today!</div>
    <div class="abs contact-phone">03 9514 -0817</div>
    <div class="abs contact-or">or</div>
    <div class="abs contact-email">info@brightpebbles.example.au</div>
  </footer>
</body>
</html>
```